Business Cards

We were billed for this because the project timed out. Please give me another designed to open this back up. I was not happy with the last designs (that I was charged for).
we are also using the logo with Renewing Water Every Ripple of the Way
Also want to utilize Where Healthy Water is our Commitment.

Contact Information for Business Card

Marlowe Stone Group Inc

```html
<!DOCTYPE html>
<html lang="en">
<head>
<meta charset="utf-8">
<title>Marlowe Stone Group — Business Card</title>
<link rel="stylesheet" href="https://fonts.googleapis.com/css2?family=Lato:ital,wght@0,400;0,700;0,900;1,700&display=swap">
<style>
  :root {
    --backdrop: #8f8f8f;
    --paper: #ffffff;
    --charcoal: #474747;
    --ink: #3d3d3d;
    --blue-deep: #1466b0;
    --blue-light: #45a3db;
    --text-light: #ffffff;
  }
  * { box-sizing: border-box; margin: 0; padding: 0; }
  html, body {
    width: 1200px; height: 1200px; overflow: hidden;
    background: var(--backdrop);
    font-family: "Lato", sans-serif;
  }
  .card {
    position: absolute; left: 281px; width: 641px; height: 365px;
    border-radius: 30px; overflow: hidden;
    box-shadow: 0 14px 24px rgba(0,0,0,0.28);
  }
  .card-front { top: 195px; background: var(--paper); }
  .card-back {
    top: 639px;
    background: linear-gradient(90deg, var(--blue-light) 0%, var(--blue-deep) 100%);
  }
  .front-art { position: absolute; inset: 0; }

  .brand-block {
    position: absolute; top: 92px; left: 0; width: 100%;
    text-align: center;
  }
  .brand-name {
    font-weight: 900; font-size: 31px; letter-spacing: 2px;
    color: var(--ink); line-height: 1;
  }
  .brand-tagline {
    margin-top: 8px; font-weight: 400; font-size: 12.5px;
    letter-spacing: 3px; color: var(--ink); text-transform: uppercase;
  }

  .holder {
    position: absolute; right: 346px; top: 220px; text-align: right;
    color: var(--text-light); letter-spacing: 0.8px;
  }
  .holder-name { font-weight: 700; font-size: 27px; letter-spacing: 1.5px; line-height: 1; }
  .holder-role { font-size: 17.5px; margin-top: 7px; line-height: 1.1; }
  .holder-address { font-size: 15px; line-height: 23.5px; margin-top: 3px; }

  .divider {
    position: absolute; left: 320px; top: 221px; width: 2px; height: 120px;
    background: var(--text-light);
  }

  .contact-list {
    position: absolute; left: 344px; top: 226px; list-style: none;
    color: var(--text-light); font-size: 15px; letter-spacing: 1px;
  }
  .contact-list li { display: flex; align-items: center; height: 24.3px; }
  .contact-list svg { width: 13px; height: 13px; margin-right: 12px; flex: none; }

  .back-name {
    position: absolute; top: 120px; left: 0; width: 100%; text-align: center;
    font-weight: 900; font-size: 46px; letter-spacing: 3px; color: var(--text-light);
    line-height: 1.05;
  }
  .back-tagline {
    position: absolute; top: 292px; left: 0; width: 100%; text-align: center;
    font-weight: 700; font-style: italic; font-size: 25px; color: var(--text-light);
  }
</style>
</head>
<body>

<section class="card card-front">
  <svg class="front-art" viewBox="0 0 641 365" aria-hidden="true">
    <path d="M0,226 C90,176 210,170 310,188 C420,208 500,212 570,185 C605,170 630,150 641,138 L641,365 L0,365 Z" fill="var(--charcoal)"/>
    <path d="M0,202 C80,158 200,150 290,176 C200,162 90,170 0,214 Z" fill="var(--blue-deep)"/>
    <path d="M430,199 C530,202 600,170 641,108 L641,122 C600,180 530,206 430,199 Z" fill="var(--blue-light)"/>
  </svg>

  <div class="brand-block">
    <div class="brand-name">MARLOWE STONE GROUP</div>
    <div class="brand-tagline">Renewing Water Every Ripple of the Way</div>
  </div>

  <div class="holder">
    <div class="holder-name">DANA WHITFIELD</div>
    <div class="holder-role">Founder &amp; CEO</div>
    <div class="holder-address">
      Marlowe Stone Group Inc<br>
      4127 Harbor Lane, Ste 300<br>
      Brookhaven, CT 06473
    </div>
  </div>

  <div class="divider"></div>

  <ul class="contact-list">
    <li>
      <svg viewBox="0 0 16 16"><path d="M3 1 L6 1 L7 5 L5 6.5 C6 9 7 10 9.5 11 L11 9 L15 10 L15 13 C15 14 14 15 13 15 C6 15 1 10 1 3 C1 2 2 1 3 1 Z" fill="var(--text-light)"/></svg>
      (555) 214-7730
    </li>
    <li>
      <svg viewBox="0 0 16 16"><rect x="3.5" y="1" width="9" height="14" rx="1.5" fill="none" stroke="var(--text-light)" stroke-width="1.8"/><circle cx="8" cy="12.3" r="1" fill="var(--text-light)"/></svg>
      (555) 382-9146
    </li>
    <li>
      <svg viewBox="0 0 16 16"><rect x="4" y="1" width="8" height="4" fill="var(--text-light)"/><rect x="1" y="6" width="14" height="6" rx="1" fill="var(--text-light)"/><rect x="4" y="10" width="8" height="5" fill="var(--text-light)" stroke="var(--charcoal)" stroke-width="1"/></svg>
      (555) 607-2258
    </li>
    <li>
      <svg viewBox="0 0 16 16"><rect x="1" y="3" width="14" height="10" fill="var(--text-light)"/><path d="M1 3 L8 9 L15 3" fill="none" stroke="var(--charcoal)" stroke-width="1.3"/></svg>
      info@marlowestonegroup.com
    </li>
    <li>
      <svg viewBox="0 0 16 16"><circle cx="8" cy="8" r="6.5" fill="none" stroke="var(--text-light)" stroke-width="1.6"/><path d="M4 5 C6 5 7 7 6 9 C5 10 5 12 6 14 M10 2.5 C9 5 11 6 13 6 M9 9 C10 11 12 11 13.5 10" fill="none" stroke="var(--text-light)" stroke-width="1.4"/></svg>
      marlowestonegroup.com
    </li>
  </ul>
</section>

<section class="card card-back">
  <div class="back-name">MARLOWE<br>STONE GROUP</div>
  <div class="back-tagline">Renewing Water Every Ripple of the Way</div>
</section>

</body>
</html>
```